Labels for Hair care products
Labels for hair care products
Project: Labels for Hair care products
Labels for Hair care products  - Salon & Spa
Creative Brief
im looking for new label designs for my hair products i will supply my logo,artwork from my pervious labels and descriptions for each product company name is: QR Scalp Works product line name is called: Grit Rebel
Salon & Spa
lets make it rough and tough looking my demographic target is age 8-30
please make sure i can edit the text, send me all files you use for each label so that i don't have any errors when opening into adobe illustrator. lets keep it about 4 to 5 color max make sure that each label clearly shows that its Shampoo, conditioner, etc

```html
<!DOCTYPE html>
<html lang="en">
<head>
<meta charset="utf-8">
<title>Grit Rebel Conditioner Labels</title>
<link href="https://fonts.googleapis.com/css2?family=Oswald:wght@400;500;700&family=Arimo:wght@400;700&display=swap" rel="stylesheet">
<style>
  :root{
    --page:#ffffff;
    --label:#050505;
    --red:#e3202a;
    --red-dark:#8e0f14;
    --blue-light:#bfe3f5;
    --blue:#2f86c2;
    --blue-dark:#0d3f73;
    --green:#8cc63f;
    --white:#ffffff;
    --gear-red:rgba(160,20,25,.35);
    --gear-teal:rgba(40,120,130,.28);
  }
  *{box-sizing:border-box;margin:0;padding:0}
  html,body{width:1200px;height:847px;overflow:hidden;background:var(--page)}
  body{position:relative;font-family:"Arimo",Arial,sans-serif}
  .label{position:absolute;top:95px;width:513px;height:685px;background:var(--label);overflow:hidden}
  .label--front{left:70px}
  .label--back{left:625px}
  .brand{position:absolute;display:flex;align-items:center;gap:8px;font-family:"Oswald",sans-serif;font-weight:500;color:var(--green);text-transform:uppercase;letter-spacing:1px;white-space:nowrap}
  .brand__dot{width:14px;height:14px;border-radius:50%;background:var(--green)}
  .label--front .brand{left:0;right:0;top:70px;justify-content:center;font-size:28px}
  .gear-art{position:absolute;border-radius:50%}
  .label--front .gear-art{left:-60px;top:110px;width:340px;height:340px;background:radial-gradient(circle,var(--gear-red) 0%,rgba(0,0,0,0) 70%)}
  .label--back .gear-art{left:200px;top:10px;width:340px;height:340px;background:radial-gradient(circle,var(--gear-teal) 0%,rgba(0,0,0,0) 70%)}
  .front__type{position:absolute;left:32px;top:228px;font-family:"Oswald",sans-serif;font-weight:700;font-size:36px;line-height:1.2;color:var(--red);text-transform:uppercase;white-space:nowrap}
  .front__name{position:absolute;left:30px;top:272px;font-family:"Oswald",sans-serif;font-weight:700;font-size:90px;line-height:1.1;letter-spacing:1px;text-transform:uppercase;white-space:nowrap;
    background:linear-gradient(180deg,var(--blue-light) 0%,var(--blue) 55%,var(--blue-dark) 100%);-webkit-background-clip:text;background-clip:text;color:transparent}
  .front__band{position:absolute;left:0;top:394px;width:500px;height:40px;background:var(--red);clip-path:polygon(0 0,100% 0,94% 100%,0 100%)}
  .front__tagline{position:absolute;left:32px;top:396px;font-family:"Oswald",sans-serif;font-weight:500;font-size:25px;line-height:36px;color:var(--white);text-transform:uppercase;white-space:nowrap}
  .front__audience{position:absolute;left:32px;top:440px;font-family:"Oswald",sans-serif;font-weight:400;font-size:17px;color:var(--white);text-transform:uppercase;white-space:nowrap}
  .stripes{position:absolute;left:0;top:462px}
  .front__footer{position:absolute;left:0;bottom:0;width:100%;height:72px;background:var(--red);display:flex;justify-content:space-between;align-items:center;padding:0 30px;font-family:"Oswald",sans-serif;font-weight:500;font-size:22px;color:var(--white);text-transform:uppercase}
  .back__header{position:absolute;left:0;top:42px;width:100%;height:58px;background:var(--red);padding-left:30px;display:flex;align-items:center;font-family:"Oswald",sans-serif;font-weight:700;font-size:34px;color:var(--white);text-transform:uppercase}
  .back__rule{position:absolute;left:0;top:100px;width:100%;height:12px;background:var(--red-dark)}
  .back__copy{position:absolute;left:30px;top:140px;width:440px;color:var(--white);font-size:13px;line-height:17px}
  .back__copy p{margin-bottom:16px}
  .back__copy h3{font-family:"Oswald",sans-serif;font-weight:500;font-size:15px;text-transform:uppercase;margin-bottom:2px}
  .back__distributor{width:150px}
  .label--back .brand{right:40px;top:560px;font-size:22px}
  .back__footer{position:absolute;left:0;bottom:0;width:100%;height:14px;background:var(--red)}
</style>
</head>
<body>
  <section class="label label--front">
    <div class="gear-art" role="img" aria-label="Faint red gear artwork"></div>
    <div class="brand"><span class="brand__dot"></span>QR Scalp Works</div>
    <p class="front__type">Conditioner</p>
    <h1 class="front__name">Grit Rebel</h1>
    <div class="front__band"></div>
    <p class="front__tagline">Salon quality without the salon</p>
    <p class="front__audience">For men and women</p>
    <svg class="stripes" width="513" height="70" viewBox="0 0 513 70">
      <polygon points="150,30 513,5 513,22 150,50" fill="#8e0f14"/>
      <polygon points="230,48 513,28 513,40 230,60" fill="#e3202a"/>
    </svg>
    <footer class="front__footer"><span>Made in USA</span><span>16 FL OZ 473 ML</span></footer>
  </section>

  <section class="label label--back">
    <div class="gear-art" role="img" aria-label="Faint teal gear artwork"></div>
    <h2 class="back__header">Conditioner</h2>
    <div class="back__rule"></div>
    <div class="back__copy">
      <p>Lorem ipsum dolor sit amet, consectetuer adipiscing elit, sed diam nonummy nibh euismod tincidunt ut laoreet dolore magna aliquam erat volutpat. Ut wisi enim ad minim veniam, quis nostrud exerci tation ullamcorper suscipit lobortis nisl</p>
      <h3>Directions :</h3>
      <p>esse molestie consequat, vel illum dolore eu feugiat nulla facilisis at vero eros et accumsan et iust</p>
      <h3>Ingredients :</h3>
      <p>Lorem ipsum dolor sit amet, consectetuer adipiscing elit, sed diam nonummy nibh euismod tincidunt ut laoreet dolore magna aliquam erat volutpat. Ut wisi enim ad minim veniam, quis nostrud exerci tation ullamcorper.</p>
      <h3>Distributed by :</h3>
      <p class="back__distributor">Lorem ipsum consectetuer adipiscing elit, sed diam nonummy nibh</p>
    </div>
    <div class="brand"><span class="brand__dot"></span>QR Scalp Works</div>
    <div class="back__footer"></div>
  </section>
</body>
</html>
```